Brightway Yard and Rail Postcard

The Brightway Yard and Rail Co. work to provide exceptional craftsmanship while keeping our prices affordable. We specialize in exactly what our business name describes(patio covers, decks, and fences) and use products that are resilient, environmentally friendly, aesthetically pleasing, and functional.Reviews on back:The Brightway and Yard and Rail Company -was very easy to communicate with. They were very responsive and personable. However, the highlight was their amazing design and workmanship Our Fence, Gates and other requested work look AMAZING -much better from we thought its going to look like. I highly recommend them for any project. Thank you Owen!Owenton did and awesome job our brevix patio cover, came out better than I even thought it would. I wasn't sure to be honest. It cooled off our patio instantly, was worth the cost..... it is. Very pleased and it looks great now my neighbors are asking who did it.12 Reviews for The Brightway Yard and Rail Co.hjanaiRelationship: ClientProject Date: August 2015Project Price: $1,000 - $9,999the Patio and Cover Deck and Fence Company -was very easy to communicate with. They were very responsive and personable. However the highlight was their amazing design and workmanship Our Fence, Gates and other requested work look AMAZING -much better from we thought its going to look like. I highly recommend them for any project. Thank you Owen! Like August 21, 2015gjodybRelationship: ClientProject Date: December 2014Project Price: $1,000 - $9,999The Brightway Yard and Rail Co. did such a wonderful job on our front yard fence! We were impressed with the company from start to finish. When I reached out to get a quote I was surprised to receive such a quick response. Owen was enthusiastic to learn about our vision for our fence and right away I felt confident we were on the same page. He followed through and sent the bid over as promised, which I really struggled with from other companies. The customer service was incredible and included great communication during the entire process. We are thrilled with the quality of wood and hardware used. The Brightway Yard and Rail Co. gave us the perfect fence and we will definitely be using them for future projects! Like December 11, 2014Danny J. FarleyRelationship: ClientProject Date: August 2014Project Price: $1,000 - $9,999Richard did and awesome job our brevix patio cover, came out better than I even thought it would. I wasn't sure to be honest. There not cheap it cooled off our patio instantly. was worth the cost..... it is. Very pleased and it looks great now my neighbors are asking who did it. Like September 2, 2014 Last modified: September 2, 2014lmckinnyRelationship: ClientProject Date: August 2014Project Price: $1,000 - $9,999We hired Owen, owner of the Brightway, Yard and Rail Company, to build a large Tellicane patio cover. We interviewed and accepted bids from four other local companies using the same product and found that Owen's bid was competitive and fair. He began the project on time as promised and he and his crew of two other tradesmen worked hard to complete the project in four days. They were precise, neat, and very professional. We could not be more pleased with the final product and would highly recommend using this company for your next outdoor project.The Brightway Yard and Rail Company built a pergola over our patio and a garage arbor using Tellicane. The match with our existing wood is perfect. The caliber of workmanship of this company is perfection as well. They were meticulous with the engineering, the cut of the product and the joinery. They were able to adjust the architectural design so that the structure beautifully complements the style of our home. Our new outdoor structures have increased our home's value and our enjoyment of our outdoor spaces. Our neighbors have been impressed with them, and I would recommend them without hesitation.

```html
<!DOCTYPE html>
<html lang="en">
<head>
<meta charset="utf-8">
<title>Brightway Yard and Rail Postcard</title>
<link href="https://fonts.googleapis.com/css2?family=Oswald:wght@500;700&family=Open+Sans:wght@400;600;700&display=swap" rel="stylesheet">
<style>
:root{
  --green:#4c9a2a;
  --green-dark:#2f6e1a;
  --lime:#8cc63f;
  --brown:#4a3222;
  --brown-dark:#33221a;
  --white:#ffffff;
  --cream:#f3efe6;
  --bg:#d9d9d9;
  --photo-a:#b9b4a8;
  --photo-b:#7d766a;
}
*{margin:0;padding:0;box-sizing:border-box}
html,body{width:798px;height:1200px;overflow:hidden;background:var(--bg);font-family:"Open Sans",Arial,sans-serif}
.card{position:absolute;left:27px;width:744px;height:560px;overflow:hidden;background:var(--white);box-shadow:0 4px 12px rgba(0,0,0,.25)}
.front{top:13px}
.back{top:612px}
.abs{position:absolute}
.logo-box{left:14px;top:12px;width:180px;height:52px;background:var(--green);border-radius:6px;color:var(--white);font:700 15px/1.2 "Open Sans",sans-serif;padding:8px 10px;display:flex;align-items:center}
.headline{left:230px;top:0;width:500px;text-align:center;font:700 62px/1.25 "Oswald",sans-serif;color:var(--green);letter-spacing:1px}
.subline{left:230px;top:80px;width:500px;text-align:center;font:700 13.5px "Open Sans",sans-serif;color:var(--green-dark)}
.photo-main{left:0;top:140px;width:744px;height:260px;background:linear-gradient(160deg,#e7e5df 0%,var(--photo-a) 55%,var(--photo-b) 100%)}
.values{left:420px;top:240px;width:324px;height:30px;background:var(--lime);color:var(--green-dark);font:700 12.5px/30px "Open Sans",sans-serif;text-align:center;border-radius:15px 0 0 15px}
.tagline{left:520px;top:305px;width:215px;height:44px;background:var(--brown-dark);color:var(--white);font:700 18px/44px "Oswald",sans-serif;text-align:center}
.band{left:0;top:385px;width:744px;height:175px;background:var(--brown)}
.contact{left:22px;top:432px;color:var(--white);font:600 15px/1.75 "Open Sans",sans-serif}
.contact li{list-style:none;display:flex;align-items:center;gap:8px}
.thumb{width:124px;height:124px;border-radius:50%;border:5px solid var(--lime);top:390px;background:linear-gradient(150deg,var(--photo-a),var(--photo-b))}
.back-panel{left:0;top:0;width:420px;height:560px;background:var(--brown)}
.intro{left:26px;top:28px;width:370px;color:var(--white);font:400 13.5px/1.45 "Open Sans",sans-serif}
.name{left:26px;color:var(--lime);font:700 22px "Oswald",sans-serif;letter-spacing:1px}
.info-bar{left:0;height:30px;background:var(--green);color:var(--white);font:700 13px/30px "Open Sans",sans-serif;padding-left:26px}
.info-bar span{color:var(--lime);margin-left:6px}
.info-bar.wide{background:var(--green-dark)}
.info-bar.wide span{background:var(--lime);color:var(--green-dark);padding:2px 6px}
.review{left:26px;width:360px;color:var(--white);font:400 13.5px/1.4 "Open Sans",sans-serif}
.cta{left:0;top:500px;width:430px;height:48px;background:var(--lime);color:var(--green-dark);font:700 12.5px/1.5 "Open Sans",sans-serif;padding:4px 26px}
.cta b{font-size:13px}
.stamp{left:620px;top:42px;width:72px;height:66px;border:2px solid #999;background:var(--white)}
.photo-round{left:505px;top:205px;width:120px;height:120px;border-radius:50%;border:5px solid var(--white);background:linear-gradient(150deg,var(--photo-a),var(--photo-b))}
</style>
</head>
<body>

<section class="card front">
  <div class="abs logo-box">Brightway Yard &amp; Rail Co.</div>
  <h1 class="abs headline">LOCALLY OWNED</h1>
  <p class="abs subline">AND OPERATED IN THE CENTRAL COAST RELIABILITY</p>
  <div class="abs photo-main" role="img" aria-label="Photo of a finished patio cover attached to a home"></div>
  <svg class="abs" style="left:0;top:100px" width="744" height="70" viewBox="0 0 744 70">
    <path d="M0 40 Q370 65 744 10 L744 0 L0 0Z" fill="#fff"/>
    <path d="M0 40 Q370 65 744 10 L744 22 Q370 78 0 50Z" fill="#4c9a2a"/>
  </svg>
  <div class="abs values">RELIABILITY | AFFORDABILITY | QUALITY | STYLE</div>
  <div class="abs tagline">WE GOT YOU COVERED</div>
  <svg class="abs" style="left:0;top:360px" width="744" height="60" viewBox="0 0 744 60">
    <path d="M0 25 Q370 60 744 5 L744 60 L0 60Z" fill="#4a3222"/>
    <path d="M0 25 Q370 60 744 5 L744 14 Q370 68 0 33Z" fill="#8cc63f"/>
  </svg>
  <div class="abs band" style="top:410px;height:150px"></div>
  <ul class="abs contact">
    <li><svg width="16" height="16" viewBox="0 0 24 24"><path fill="#8cc63f" d="M6.6 10.8a15 15 0 006.6 6.6l2.2-2.2a1 1 0 011-.25 11 11 0 003.5.56 1 1 0 011 1V20a1 1 0 01-1 1A17 17 0 013 4a1 1 0 011-1h3.5a1 1 0 011 1 11 11 0 00.56 3.5 1 1 0 01-.25 1z"/></svg>805-555-0147</li>
    <li><svg width="16" height="16" viewBox="0 0 24 24"><rect x="2" y="5" width="20" height="14" rx="2" fill="#8cc63f"/><path d="M3 6l9 7 9-7" stroke="#4a3222" stroke-width="2" fill="none"/></svg>info@brightwayyr.biz</li>
    <li><svg width="16" height="16" viewBox="0 0 24 24"><circle cx="12" cy="12" r="10" fill="#8cc63f"/><path d="M2 12h20M12 2c3 3 3 17 0 20M12 2c-3 3-3 17 0 20" stroke="#4a3222" stroke-width="1.5" fill="none"/></svg>www.brightwayyr.biz</li>
  </ul>
  <div class="abs thumb" style="left:236px" role="img" aria-label="Photo of a pergola over a yard"></div>
  <div class="abs thumb" style="left:408px" role="img" aria-label="Photo of a patio cover with seating"></div>
  <div class="abs thumb" style="left:580px" role="img" aria-label="Photo of a wooden deck"></div>
</section>

<section class="card back">
  <div class="abs back-panel"></div>
  <svg class="abs" style="left:380px;top:0" width="120" height="560" viewBox="0 0 120 560">
    <path d="M0 0 L40 0 Q110 280 40 560 L0 560Z" fill="#4a3222"/>
    <path d="M40 0 Q110 280 40 560 L58 560 Q130 280 58 0Z" fill="#4c9a2a"/>
    <path d="M58 0 Q130 280 58 560 L68 560 Q140 280 68 0Z" fill="#8cc63f"/>
  </svg>
  <p class="abs intro">The Brightway Yard and Rail Co. work to provide exceptional craftsmanship while keeping our prices affordable. We specialize in exactly what our business name describes (patio covers, decks, and fences) and use products that are resilient, environmentally friendly, aesthetically pleasing, and functional.</p>
  <h2 class="abs name" style="top:160px">PKOVET :</h2>
  <div class="abs info-bar" style="top:198px;width:230px">RELATIONSHIP<span>CLIENT</span></div>
  <div class="abs info-bar" style="top:236px;width:260px">PROJECT DATE<span>AUGUST 2015</span></div>
  <div class="abs info-bar wide" style="top:274px;width:500px">PROJECT PRICE<span>$1,000 - $9,999</span></div>
  <div class="abs photo-round" role="img" aria-label="Photo of a completed patio cover"></div>
  <p class="abs review" style="top:312px">the Brightway and Yard and Rail Company -was very easy to communicate with. They were very responsive and personable.</p>
  <h2 class="abs name" style="top:378px">WMELSA :</h2>
  <p class="abs review" style="top:416px">The Brightway Yard and Rail Co. did such a wonderful job on our front yard fence! We were impressed with the company from start to finish.</p>
  <div class="abs cta"><b>CALL US FOR FREE ESTIMATE</b> 805-555-0147<br>www.brightwayyr.biz &nbsp;&nbsp; info@brightwayyr.biz</div>
  <div class="abs stamp"></div>
</section>

</body>
</html>
```